Website for a company offering full serivce charging solutions for electric cars

The company "vorn-werk" (english: "front-works") offering all-in-one-solutions for charging infrastructure for electric mobility.

There are four products:
1- Wallboxes for single-family homes
2- Solutions for property devloper/-management for property parking space
3- All-in-one-charging solution for municipalities/communities
4- Solutions for tourism/hotels/holiday appartments

The Website structure:
1. Main Page
2.1. Product Page Single Homes
2.2. Product Page Property Management / Parking
2.3. Product Page Municipality
2.4. Product Page Tourism
3. Contact Form / Request for information
4. Imprint / Legal

The Website should be built on Wordpress with a powerful possibility to simply add/modify specific landing pages.

We would like you to implement the website later and also maintain it if possible, but we would be able to do minor modifications by ourselfs (for A/B-Testing)

The website should be clear and simple, easy to understand.
Target group is mainly B2C without deeper knowledge of that topic.

It should suggest, that we will provide a very simple way to get the charging infrastructure done.

We need a contact form, maybe we will use Leadmill later.

Attached you will find a draft of the main page and a landing page (for 2.2) - it is just the content, please ignore the design. We would love to let you create a suitable design.
Also you will find some drafts a bit different for the same story.

I added also a few stock photos, but they don't need to be used! If you have better ideas, you are welcome!

Charging/Electric mobility

Sans Serif

• Based on Wordpress, and the designer should be able to implement it on Wordpress on a later step

```html
<!DOCTYPE html>
<html lang="en">
<head>
<meta charset="utf-8">
<title>vorn-werk.de – Charging Solutions</title>
<link href="https://fonts.googleapis.com/css2?family=Exo+2:wght@500;600&family=Outfit:wght@300;400;500&display=swap" rel="stylesheet">
<style>
:root{
  --navy:#121826;
  --pink:#e0249f;
  --purple:#8a5cd6;
  --grad:linear-gradient(90deg,#e0249f 0%,#b23cc2 60%,#8a5cd6 100%);
  --light:#e9ebf0;
  --white:#ffffff;
  --ink:#151a26;
  --muted:#3a3f4b;
  --green:#2aa52e;
}
*{margin:0;padding:0;box-sizing:border-box}
html,body{width:1200px;height:3799px;overflow:hidden}
body{position:relative;font-family:'Outfit',sans-serif;color:var(--ink);background:var(--white)}
.head{font-family:'Exo 2',sans-serif;font-weight:600}
.section{position:absolute;left:0;width:1200px;overflow:hidden}
.btn{position:absolute;display:flex;align-items:center;justify-content:center;background:var(--grad);color:#fff;font-family:'Exo 2',sans-serif;font-weight:600;font-size:16px;border-radius:14px 0 14px 0;}
.brand{display:flex;align-items:center;gap:10px;color:#fff;font-family:'Outfit',sans-serif;font-weight:500;font-size:25px}
.brand-dot{width:26px;height:26px;border-radius:50%;background:var(--pink)}
.media{position:absolute}

/* nav */
.nav{top:0;height:83px;background:var(--navy)}
.nav .brand{position:absolute;left:174px;top:22px}
.nav-links{position:absolute;left:469px;top:30px;color:#e6e8ee;font-size:15px}
.nav-links span{position:absolute;white-space:nowrap}
.lang-sep{position:absolute;left:964px;top:28px;width:1px;height:22px;background:#4a5063}

/* hero */
.hero{top:83px;height:436px}
.hero-photo{left:0;top:0;width:1200px;height:436px;background:linear-gradient(100deg,#cfd6dc 0%,#9aa5ad 22%,#5f6a66 40%,#4d5a4a 60%,#3c7a2c 78%,#2f5f22 100%)}
.hero-shade{left:0;top:0;width:1200px;height:436px;background:linear-gradient(90deg,rgba(0,0,0,0) 30%,rgba(0,0,0,.35) 70%)}
.hero h1{position:absolute;left:500px;top:118px;font-size:40px;color:#fff;font-weight:600;letter-spacing:.5px}
.hero p{position:absolute;left:503px;top:170px;width:470px;font-size:16px;line-height:28px;color:#fff}
.slider-num{position:absolute;color:#fff;font-size:17px}
.slider-line{position:absolute;left:1013px;top:170px;width:1px;height:110px;background:#fff}

/* welcome */
.welcome{top:519px;height:494px;background:var(--light)}
.welcome .kicker{position:absolute;left:174px;top:107px;color:var(--pink);font-family:'Exo 2',sans-serif;font-size:20px;font-weight:500}
.welcome h2{position:absolute;left:172px;top:130px;font-size:52px;color:var(--ink)}
.welcome p{position:absolute;left:174px;width:420px;font-size:13.5px;line-height:24px;color:var(--muted)}
.info-card{position:absolute;left:685px;top:57px;width:342px;height:378px;background:var(--navy);border-radius:6px}
.info-card h3{position:absolute;left:21px;top:24px;font-size:27px;color:#fff;font-weight:500}
.field{position:absolute;left:20px;width:297px;height:47px;background:#fff;border-radius:4px;padding:0 14px;display:flex;align-items:center;font-size:15px;color:#4a5060}

/* wallbox */
.wallbox{top:1013px;height:395px;background:var(--navy)}
.wallbox h2{position:absolute;left:172px;top:56px;font-size:41px;line-height:47px;color:#fff;font-weight:600}
.wallbox p{position:absolute;left:172px;width:440px;font-size:13.5px;line-height:24px;color:#fff}
.wb-art{left:615px;top:85px;width:412px;height:266px;border-radius:120px 120px 60px 60px;background:linear-gradient(90deg,#e0249f,#a94ad0 60%,#8a5cd6)}

/* offers */
.offers{top:1408px;height:1032px;background:#fff}
.card{position:absolute;top:62px;width:270px;background:#fff;border-radius:6px;box-shadow:0 4px 14px rgba(20,25,40,.14)}
.card-head{height:56px;background:var(--grad);border-radius:6px 6px 0 0;color:#fff;display:flex;align-items:center;justify-content:center;font-family:'Exo 2',sans-serif;font-weight:500;font-size:19px}
.card ul{list-style:none;padding:18px 16px 0 12px}
.card li{position:relative;padding-left:22px;font-size:11.6px;line-height:16px;color:#2b303c;margin-bottom:14px}
.card li.tick::before{content:"";position:absolute;left:2px;top:2px;width:11px;height:6px;border-left:3px solid var(--green);border-bottom:3px solid var(--green);transform:rotate(-45deg)}
.card li.sub{padding-left:38px}
.card li.sub::before{content:"";position:absolute;left:22px;top:4px;border-left:6px solid #2b303c;border-top:4px solid transparent;border-bottom:4px solid transparent}

/* tenants */
.tenants{top:2440px;height:392px;background:var(--navy)}
.tenant-photo{left:165px;top:12px;width:385px;height:365px;border-radius:70px 40px 80px 40px;background:linear-gradient(140deg,#d8e2ee 0%,#b9c6d6 40%,#7a8798 70%,#e9edf2 100%)}
.tenants h2{position:absolute;left:609px;top:57px;font-size:40px;line-height:47px;color:#fff}
.tenants h4{position:absolute;left:609px;top:157px;font-size:21px;color:#fff;font-weight:500}
.tenants p{position:absolute;left:609px;top:203px;width:430px;font-size:13.5px;line-height:24px;color:#fff}

/* contact */
.contact{top:2832px;height:535px;background:#fff}
.contact-photo{left:640px;top:0;width:560px;height:535px;background:linear-gradient(90deg,#ffffff 0%,#eef0f2 25%,#d9dde2 55%,#b8bfc6 100%)}
.contact .kicker{position:absolute;left:171px;top:76px;color:var(--pink);font-family:'Exo 2',sans-serif;font-size:21px;font-weight:500}
.contact h2{position:absolute;left:170px;top:103px;font-size:50px;color:var(--ink)}
.cfield{position:absolute;font-size:14.5px;color:#2b303c;border-bottom:1.5px solid #3a3f4b;padding-bottom:14px}

/* footer */
.footer{top:3367px;height:432px;background:var(--navy)}
.footer .brand{position:absolute;left:172px;top:80px}
.footer .about{position:absolute;left:172px;top:133px;width:280px;font-size:14px;line-height:27px;color:#fff}
.social{position:absolute;top:258px;width:30px;height:30px;border-radius:50%;background:#fff}
.fcol{position:absolute;top:78px}
.fcol h5{font-family:'Exo 2',sans-serif;font-weight:500;font-size:18px;color:var(--pink);margin-bottom:16px}
.fcol ul{list-style:none}
.fcol li{position:relative;padding-left:13px;font-size:14.5px;color:#fff;height:39px;line-height:20px}
.fcol li::before{content:"";position:absolute;left:0;top:7px;border-left:4px solid var(--pink);border-top:3px solid transparent;border-bottom:3px solid transparent}
.footer-rule{position:absolute;left:171px;top:373px;width:857px;height:1px;background:#3a4052}
.copy{position:absolute;left:0;width:1200px;top:393px;text-align:center;font-size:12.5px;color:#fff}
.copy b{color:var(--pink);font-weight:400}
</style>
</head>
<body>

<header class="section nav">
  <div class="brand"><span class="brand-dot"></span>vorn-werk.de</div>
  <nav class="nav-links">
    <span style="left:0">Solutions</span>
    <span style="left:111px">Company</span>
    <span style="left:221px">Services</span>
    <span style="left:324px">Career</span>
    <span style="left:414px">Contact</span>
    <span style="left:512px">Eng ▾</span>
  </nav>
  <div class="lang-sep"></div>
</header>

<section class="section hero">
  <div class="media hero-photo" role="img" aria-label="Charging station with cable plugged into a green electric car, city skyline behind"></div>
  <div class="media hero-shade"></div>
  <h1 class="head">vorn-werk ist Ihr Partner</h1>
  <p>When loading is not only supposed to be easy, but also when the implementation is to come from a single source</p>
  <a class="btn" style="left:503px;top:243px;width:145px;height:41px">Know More</a>
  <span class="slider-num" style="left:1000px;top:134px">01</span>
  <div class="slider-line"></div>
  <span class="slider-num" style="left:1000px;top:280px">04</span>
</section>

<section class="section welcome">
  <div class="kicker">Welcome to</div>
  <h2 class="head">vorn-werk.de</h2>
  <p style="top:202px">When loading is not only supposed to be easy, but also when the implementation is to come from a single source</p>
  <p style="top:261px">We offer solutions for private customers, business customers and municipalities who want to get a smart charging solution</p>
  <a class="btn" style="left:177px;top:333px;width:146px;height:41px">Read More</a>
  <form class="info-card">
    <h3 class="head">Request for information</h3>
    <div class="field" style="top:71px">Name</div>
    <div class="field" style="top:128px">Email</div>
    <div class="field" style="top:185px">Location</div>
    <div class="field" style="top:241px">Phone</div>
    <a class="btn" style="left:96px;top:307px;width:148px;height:41px">Submit Now</a>
  </form>
</section>

<section class="section wallbox">
  <h2 class="head">Quickly and easily to<br>your private wall box</h2>
  <p style="top:166px">From taking stock, to advising on possible solutions, to installation and commissioning, everything from ONE source.</p>
  <p style="top:225px">And if you wish, we will also be happy to lend you the wall box for a small usage fee.</p>
  <a class="btn" style="left:174px;top:293px;width:146px;height:41px">Read More</a>
  <div class="media wb-art" role="img" aria-label="Charging plug in front of a pink and purple car outline illustration"></div>
</section>

<section class="section offers">
  <div class="card" style="left:171px">
    <div class="card-head">As a private customer</div>
    <ul>
      <li class="tick">Analysis of the situation with extensive advice on the possibilities of implementation</li>
      <li class="tick">Checking and acceptance of the registration for available funding opportunities</li>
      <li class="tick">Selection of smart wallbox solutions, suitable for your vehicle and your needs</li>
      <li class="tick">Installation including all necessary materials and activities (breakthroughs, earthworks, etc.)</li>
      <li class="tick">Commissioning and instruction in charging technology</li>
      <li class="tick">Annual technical maintenance according to NRVS3</li>
      <li class="tick">Repair service, taking into account the applicable warranty claims</li>
      <li class="tick">Installation including all necessary materials and activities (breakthroughs, earthworks, etc.)</li>
      <li class="tick">Commissioning and instruction in charging technology</li>
      <li class="tick">Annual technical maintenance according to NRVS3</li>
      <li class="tick">Repair service, taking into account the applicable warranty claims</li>
    </ul>
  </div>
  <div class="card" style="left:464px">
    <div class="card-head">As a business customer</div>
    <ul>
      <li class="tick">Carrying out an individual needs analysis including determination of the requirements for:</li>
      <li class="sub">House and real estate management service and trading companies</li>
      <li class="sub">Hotel and accommodation establishments</li>
      <li class="sub">Parking and car park operators</li>
      <li class="sub">Tourism, sports and</li>
      <li>Recreational facilities</li>
      <li class="tick">Planning and project planning of the installation effort including material consumption</li>
      <li class="tick">&nbsp;</li>
      <li>Leasing or buying the hardware</li>
      <li class="tick">Standard-compliant installation of the charging infrastructure including breakthrough, fire protection and earthworks</li>
      <li class="tick">In existing buildings, integration of the charging infrastructure into the building system technology and, if necessary, adjustment of the grid connection</li>
      <li class="tick">Commissioning of the system including test and measurement reports</li>
      <li class="tick">Recurring technical inspection of the system according to NRVS 3</li>
      <li class="tick" style="margin-bottom:8px">Exchange and repair service support with the monthly</li>
      <li class="tick">Usage billing and integration into your existing billing systems</li>
      <li class="tick">OR direct billing to users</li>
    </ul>
  </div>
  <div class="card" style="left:758px;height:701px">
    <div class="card-head">As a municipality</div>
    <ul>
      <li class="tick">Conception of possible charging infrastructures within your municipality</li>
      <li class="tick">Planning and project management including all official approval procedures and application for subsidies</li>
      <li class="tick">Professional installation and commissioning</li>
      <li class="tick">Regular maintenance according to regulation repair and customer service</li>
      <li class="tick" style="margin-bottom:8px">Direct billing with the user</li>
      <li class="tick" style="margin-bottom:8px">Community participation in sales</li>
      <li class="tick">Possibility of integrating bonus programs that promote local retail of grants</li>
      <li class="tick">Professional installation and commissioning</li>
      <li class="tick">Regular maintenance according to regulation repair and customer service</li>
      <li class="tick">Direct billing with the user</li>
      <li>Community participation in sales</li>
      <li class="tick">Possibility of integrating bonus programs that promote local retail</li>
    </ul>
  </div>
</section>

<section class="section tenants">
  <div class="media tenant-photo" role="img" aria-label="Close-up of a charging connector plugged into a white electric car, wind turbine in the background"></div>
  <h2 class="head">Offer your tenants,<br>employees</h2>
  <h4 class="head">Customers and guests even more comfort</h4>
  <p>We advise, plan and implement the solution that makes your company, residential park, tourism facility even more attractive</p>
  <a class="btn" style="left:609px;top:269px;width:146px;height:41px">Read More</a>
</section>

<section class="section contact">
  <div class="media contact-photo" role="img" aria-label="Woman plugging a charging cable into a white electric car beside modern buildings"></div>
  <div class="kicker">Contact Us</div>
  <h2 class="head">Get In Touch</h2>
  <div class="cfield" style="left:171px;top:197px;width:255px">First Name</div>
  <div class="cfield" style="left:445px;top:197px;width:254px">Last Name</div>
  <div class="cfield" style="left:171px;top:270px;width:255px">Email</div>
  <div class="cfield" style="left:442px;top:270px;width:257px">Phone</div>
  <div class="cfield" style="left:171px;top:340px;width:528px;padding-bottom:62px">Your Message</div>
  <a class="btn" style="left:174px;top:448px;width:130px;height:41px">Send Now</a>
</section>

<footer class="section footer">
  <div class="brand"><span class="brand-dot"></span>vorn-werk.de</div>
  <p class="about">When loading is not only supposed to be easy, but also when the implementation is to come from a single source</p>
  <span class="social" style="left:172px" aria-label="Social profile 1"></span>
  <span class="social" style="left:215px" aria-label="Social profile 2"></span>
  <span class="social" style="left:258px" aria-label="Social profile 3"></span>
  <div class="fcol" style="left:537px">
    <h5>Useful links</h5>
    <ul><li>Conditions</li><li>Data protection</li><li>imprint</li><li>Contact</li><li>Career</li><li>FAQs</li></ul>
  </div>
  <div class="fcol" style="left:738px">
    <h5>Quick Links</h5>
    <ul><li>Solutions</li><li>Company</li><li>Services</li><li>Career</li><li>Contact</li></ul>
  </div>
  <div class="fcol" style="left:917px">
    <h5>Services</h5>
    <ul><li>Nullam sagittis</li><li>Posuere eros</li><li>bibendum nec</li><li>Eros gravida</li><li>Posuere lorem</li></ul>
  </div>
  <div class="footer-rule"></div>
  <p class="copy">© 2022 <b>vorn-werk.de</b>. All right reserved</p>
</footer>

</body>
</html>
```